Corvane Electrical Solutions

On one side. LOGO (underneath:) Commercial Industrial Residential

- NAME & CONTACT DETAILS

Marcus T. Hollings
Project Manager

(Cell icon) (441) 582-6197
(Email icon) cvnelectricalsoultions@mailventra.com
(Facebook & Instagram icons )@cvnelectricalsolutions

Other side: LOGO - underneath ELECTRICAL CONSTRUCTION & MAINTENANCE . LED LIGHTING & AUTOMATION . LIFE SAFETY SYSTEMS (FIRE ALARM / SECURITY) . DATA & COMMUNICATION

```html
<!DOCTYPE html>
<html lang="en">
<head>
<meta charset="utf-8">
<title>Corvane Electrical Solutions – Business Card</title>
<link rel="stylesheet" href="https://fonts.googleapis.com/css2?family=Montserrat:wght@500&family=Roboto:wght@400&family=Saira+Condensed:wght@600&display=swap">
<style>
  :root {
    --backdrop: #d8d5d1;
    --card: #efeeeb;
    --card-edge: #ffffff;
    --teal: #1b5a6d;
    --ink: #2f3336;
    --rule: #1e4d63;
  }
  * { margin: 0; padding: 0; box-sizing: border-box; }
  html, body {
    width: 1200px; height: 1054px; overflow: hidden;
    background: var(--backdrop);
  }
  .card {
    position: absolute; left: 100px; top: 227px;
    width: 1000px; height: 600px;
    background: var(--card);
    border: 1px solid var(--card-edge);
    box-shadow: 0 10px 30px rgba(0,0,0,0.12);
  }
  .brand {
    position: absolute; left: 48px; top: 72px;
    display: flex; align-items: center; gap: 22px;
  }
  .brand-square {
    width: 86px; height: 86px; background: var(--teal);
  }
  .brand-name {
    font-family: "Montserrat", sans-serif; font-weight: 500;
    color: var(--teal); font-size: 31px; line-height: 38px;
    letter-spacing: 3px; text-transform: uppercase;
  }
  .services {
    position: absolute; left: 48px; top: 193px;
    font-family: "Montserrat", sans-serif; font-weight: 500;
    color: var(--teal); font-size: 23px; letter-spacing: 1.6px;
    text-transform: uppercase; word-spacing: 4px;
  }
  .services .sep { margin: 0 14px; }
  .person {
    position: absolute; left: 48px; top: 380px; right: 48px;
  }
  .person-name {
    font-family: "Saira Condensed", sans-serif; font-weight: 600;
    color: var(--teal); font-size: 42px; line-height: 46px;
  }
  .person-role {
    display: flex; align-items: flex-end; gap: 6px;
    font-family: "Roboto", sans-serif; color: var(--ink);
    font-size: 24px; line-height: 30px;
  }
  .person-role .rule {
    flex: 1; height: 3px; background: var(--rule); margin-bottom: 5px;
  }
  .contacts {
    position: absolute; left: 48px; top: 478px;
    font-family: "Roboto", sans-serif; color: var(--ink); font-size: 24px;
  }
  .contact-row {
    display: flex; align-items: center; height: 38px;
  }
  .contact-row svg { width: 24px; height: 24px; margin-right: 26px; fill: var(--teal); }
  .social-dot {
    width: 22px; height: 22px; border-radius: 50%;
    background: var(--teal); margin: 0 12px 0 20px;
  }
</style>
</head>
<body>
  <div class="card">
    <div class="brand">
      <div class="brand-square"></div>
      <div class="brand-name">Corvane<br>Electrical<br>Solutions</div>
    </div>
    <div class="services">Commercial<span class="sep">|</span>Industrial<span class="sep">|</span>Residential</div>

    <div class="person">
      <div class="person-name">Marcus T. Hollings</div>
      <div class="person-role"><span>Project Manager</span><span class="rule"></span></div>
    </div>

    <div class="contacts">
      <div class="contact-row">
        <svg viewBox="0 0 24 24" aria-hidden="true"><path d="M3 9c0-3 4-5 9-5s9 2 9 5v2h-5V9c-1-1-7-1-8 0v2H3zM7 12h10l3 8H4z"/></svg>
        <span>(441) 582-6197</span>
      </div>
      <div class="contact-row">
        <svg viewBox="0 0 24 24" aria-hidden="true"><path d="M2 5h20v14H2zM4 7v1l8 5 8-5V7l-8 5z"/></svg>
        <span>cvnelectricalsoultions@mailventra.com</span>
        <span class="social-dot"></span>
        <span>@cvnelectricalsolutions</span>
      </div>
    </div>
  </div>
</body>
</html>
```